A Speech Therapy Business needs to update their logo

I need an update to the font and color of my logo to look more appealing. I am looking to open a private practice as a Speech Language Pathologist that caters to adults and children. It needs to be sophisticated and friendly at the same time. I want to keep the silhouette in my logo as is, just update the font and color for "Brightpaths".
Industry/Entity Type
Business
Contact Information for Business Card
I want the business card to have my logo, my name (Dorota Valk, CCC-SLP, TSSLD) and that I am a Bilingual Speech Language Pathologist. Also, include my phone number, (555) 271-8390. Include my website, Brightpathsslp.example, and email address, dorotavalk@brightpathsslp.example
Look and feel
Each slider illustrates characteristics of the customer's brand and the style your logo design should communicate.

```html
<!DOCTYPE html>
<html lang="en">
<head>
<meta charset="utf-8">
<title>Brightpaths – Business Card</title>
<link href="https://fonts.googleapis.com/css2?family=Open+Sans:wght@300;400;600&display=swap" rel="stylesheet">
<style>
  :root {
    --page-bg: #ffffff;
    --card-bg: #f5f5f4;
    --card-edge: #e4e4e2;
    --ink: #1c1c1c;
    --ink-soft: #4a4a4a;
    --brand: #9a3934;
  }
  * { margin: 0; padding: 0; box-sizing: border-box; }
  html, body {
    width: 1200px;
    height: 848px;
    overflow: hidden;
    background: var(--page-bg);
    font-family: "Open Sans", Arial, sans-serif;
  }
  .card {
    position: absolute;
    left: 100px;
    top: 146px;
    width: 1000px;
    height: 556px;
    background: var(--card-bg);
    border: 1px solid var(--card-edge);
    border-radius: 22px;
  }
  .holder {
    position: absolute;
    left: 73px;
    top: 58px;
    text-align: right;
  }
  .holder-name {
    font-weight: 300;
    font-size: 70px;
    line-height: 1;
    letter-spacing: 1px;
    color: var(--ink);
    text-transform: uppercase;
  }
  .holder-credentials {
    margin-top: 4px;
    font-weight: 400;
    font-size: 23px;
    color: var(--ink-soft);
  }
  .holder-role {
    position: absolute;
    left: 614px;
    top: 80px;
    font-size: 21px;
    line-height: 26px;
    color: var(--ink-soft);
  }
  .brand {
    position: absolute;
    left: 64px;
    top: 388px;
    display: flex;
    align-items: center;
    gap: 16px;
  }
  .brand-dot {
    width: 34px;
    height: 34px;
    border-radius: 50%;
    background: var(--brand);
  }
  .brand-name {
    font-weight: 600;
    font-size: 54px;
    line-height: 1;
    color: var(--brand);
  }
  .contact {
    position: absolute;
    left: 614px;
    top: 402px;
    list-style: none;
    color: var(--ink-soft);
  }
  .contact-phone { font-size: 26px; line-height: 34px; }
  .contact-web,
  .contact-email { font-size: 20px; line-height: 28px; }
</style>
</head>
<body>
  <div class="card">
    <div class="holder">
      <h1 class="holder-name">Dorota Valk</h1>
      <p class="holder-credentials">CCC-SLP, TSSLD</p>
    </div>

    <p class="holder-role">Bilingual Speech<br>Language Pathologist</p>

    <div class="brand">
      <span class="brand-dot"></span>
      <span class="brand-name">Brightpaths</span>
    </div>

    <ul class="contact">
      <li class="contact-phone">(555) 271-8390</li>
      <li class="contact-web">brightpathsslp.example</li>
      <li class="contact-email">dorotavalk@brightpathsslp.example</li>
    </ul>
  </div>
</body>
</html>
```